International Shipping Company requires business card designs

We are a company based in Dubai UAE with our core business being shipping and container services. Our details can be found at www.coralwakefreight.com

We are not looking for a design that necessarily involves "ships or other shipping pictures", although some reference to the business in design or colour is encouraged.

Overall design of the card must be smart and depict the company which is very professional. Fonts, colours and layout must be very contemporary in look.

Shipping

```html
<!DOCTYPE html>
<html lang="en">
<head>
<meta charset="utf-8">
<title>Coral Wake International Shipping – Business Card</title>
<link rel="stylesheet" href="https://fonts.googleapis.com/css2?family=Arimo:wght@400;700&display=swap">
<style>
  :root {
    --backdrop: #e6e7e9;
    --card: #ffffff;
    --brand-blue: #2c80c3;
    --brand-navy: #2b2f80;
    --wave-blue: #2a8fd2;
    --wave-light: #9ccbeb;
    --ink: #2b2b2b;
    --on-navy: #ffffff;
    --on-navy-soft: #8ec7f0;
  }
  * { box-sizing: border-box; margin: 0; padding: 0; }
  html, body {
    width: 1200px; height: 951px; overflow: hidden;
    background: var(--backdrop);
    font-family: "Arimo", Arial, sans-serif;
  }
  .card {
    position: absolute; left: 220px;
    width: 760px; height: 434px;
    background: var(--card);
    border-radius: 26px;
    overflow: hidden;
    box-shadow: 0 6px 18px rgba(0,0,0,0.18);
  }
  .card--front { top: 24px; }
  .card--back { top: 494px; }

  .brand { position: absolute; display: flex; align-items: center; white-space: nowrap; }
  .brand__mark {
    border-radius: 50%;
    background: var(--brand-navy);
    flex: none;
  }
  .brand__text { color: var(--brand-blue); font-weight: 700; line-height: 1; }
  .brand__name { display: block; letter-spacing: 1px; }
  .brand__sub { display: block; }

  .card--front .brand { left: 62px; top: 118px; }
  .card--front .brand__mark { width: 118px; height: 118px; margin-right: 22px; }
  .card--front .brand__name { font-size: 68px; }
  .card--front .brand__sub { font-size: 24px; margin-top: 6px; }

  .website {
    position: absolute; left: 116px; top: 296px;
    font-size: 22px; letter-spacing: 2.5px; color: var(--ink);
  }

  .card--back .brand { left: 140px; top: 30px; }
  .card--back .brand__mark { width: 90px; height: 90px; margin-right: 18px; }
  .card--back .brand__name { font-size: 54px; }
  .card--back .brand__sub { font-size: 19px; margin-top: 5px; }

  .wave { position: absolute; inset: 0; }

  .person { position: absolute; left: 150px; top: 252px; color: var(--on-navy); }
  .person__name { font-size: 26px; }
  .person__role { font-size: 17px; color: var(--on-navy-soft); margin-top: 2px; }
  .address {
    position: absolute; left: 150px; top: 330px;
    display: flex; gap: 10px; color: var(--on-navy);
    font-size: 19px; line-height: 1.25;
  }
  .divider {
    position: absolute; left: 388px; top: 264px;
    width: 2px; height: 140px; background: var(--on-navy);
  }
  .contacts {
    position: absolute; left: 408px; top: 276px;
    list-style: none; color: var(--on-navy); font-size: 19px;
  }
  .contacts li { display: flex; align-items: center; gap: 10px; height: 24px; }
  .icon { width: 16px; height: 16px; flex: none; }
</style>
</head>
<body>

<section class="card card--front" aria-label="Card front">
  <div class="brand">
    <span class="brand__mark"></span>
    <span class="brand__text">
      <span class="brand__name">CORAL WAKE</span>
      <span class="brand__sub">INTERNATIONAL SHIPPING (L.L.C.)</span>
    </span>
  </div>
  <p class="website">www.coralwakefreight.com</p>
</section>

<section class="card card--back" aria-label="Card back">
  <svg class="wave" viewBox="0 0 760 434" aria-hidden="true">
    <path d="M0 196 C 200 170, 430 250, 760 176 L760 200 C 430 270, 200 192, 0 216 Z" fill="var(--wave-light)"/>
    <path d="M0 206 C 210 184, 430 268, 760 196 L760 226 C 430 292, 200 212, 0 232 Z" fill="var(--wave-blue)"/>
    <path d="M0 226 C 210 206, 430 290, 760 220 L760 434 L0 434 Z" fill="var(--brand-navy)"/>
  </svg>

  <div class="brand">
    <span class="brand__mark"></span>
    <span class="brand__text">
      <span class="brand__name">CORAL WAKE</span>
      <span class="brand__sub">INTERNATIONAL SHIPPING (L.L.C.)</span>
    </span>
  </div>

  <div class="person">
    <p class="person__name">Marcus Trelane</p>
    <p class="person__role">director</p>
  </div>

  <div class="address">
    <svg class="icon" viewBox="0 0 16 16" aria-hidden="true" style="margin-top:3px">
      <path d="M8 1 L15 8 H12.5 V15 H9.5 V10.5 H6.5 V15 H3.5 V8 H1 Z" fill="var(--on-navy-soft)"/>
    </svg>
    <p>1480 Harbor Quay Rd<br>Austen, TX 78105</p>
  </div>

  <span class="divider"></span>

  <ul class="contacts">
    <li>
      <svg class="icon" viewBox="0 0 16 16" aria-hidden="true"><circle cx="8" cy="8" r="8" fill="var(--on-navy-soft)"/><path d="M5 4 L7 4 L7.6 6.4 L6.6 7.2 C7.2 8.4 7.8 9 9 9.6 L9.8 8.6 L12 9.2 L12 11 C8 11.4 4.6 8 5 4 Z" fill="var(--brand-navy)"/></svg>
      512-004-2310
    </li>
    <li>
      <svg class="icon" viewBox="0 0 16 16" aria-hidden="true"><circle cx="8" cy="8" r="8" fill="var(--on-navy-soft)"/><rect x="5" y="4" width="6" height="3" fill="var(--brand-navy)"/><rect x="4" y="7" width="8" height="4" rx="1" fill="var(--brand-navy)"/></svg>
      512-004-2311
    </li>
    <li>
      <svg class="icon" viewBox="0 0 16 16" aria-hidden="true"><circle cx="8" cy="8" r="8" fill="var(--on-navy-soft)"/><rect x="4" y="5" width="8" height="6" fill="var(--brand-navy)"/><path d="M4 5 L8 8.5 L12 5" stroke="var(--on-navy-soft)" fill="none"/></svg>
      info@coralwakefreight.com
    </li>
    <li>
      <svg class="icon" viewBox="0 0 16 16" aria-hidden="true"><circle cx="8" cy="8" r="8" fill="var(--on-navy-soft)"/></svg>
      www.coralwakefreight.com
    </li>
  </ul>
</section>

</body>
</html>
```